Falcrest security business card

Looking for a business card for my security company

Target Market(s)

Security

Industry/Entity Type

Security

Contact Information for Business Card

Name - Gil Marston. Title - General manager - direct 314 862.4490 website www. falcrestsecurityservices.example email - gil@ falcrestsecurityservices.example

Requirements
Must have
• Logo attached

```html
<!DOCTYPE html>
<html lang="en">
<head>
<meta charset="utf-8">
<title>Falcrest Security Business Card</title>
<link href="https://fonts.googleapis.com/css2?family=Cinzel:wght@700&family=Roboto:wght@400;500;700&display=swap" rel="stylesheet">
<style>
  :root {
    --ink: #0d0d0d;
    --gold: #d4a636;
    --gold-light: #f2d27a;
    --paper: #ffffff;
    --stage: #ececec;
    --shadow-grey: #3a3a3a;
    --text-dark: #222222;
  }
  * { box-sizing: border-box; margin: 0; padding: 0; }
  html, body { width: 800px; height: 1200px; overflow: hidden; }
  body {
    background: var(--stage);
    font-family: "Roboto", Arial, sans-serif;
    position: relative;
  }
  .card {
    position: absolute;
    left: 50px;
    width: 700px;
    height: 400px;
    overflow: hidden;
    box-shadow: 0 6px 18px rgba(0,0,0,0.18);
  }
  .card--front { top: 150px; background: var(--ink); }
  .card--back { top: 630px; background: var(--paper); }

  .brand-name {
    font-family: "Cinzel", Georgia, serif;
    font-weight: 700;
    color: var(--gold);
    letter-spacing: 3px;
    line-height: 1;
  }
  .brand-mark {
    display: inline-block;
    border-radius: 50%;
    background: var(--gold);
  }

  /* Front */
  .front-brand {
    position: absolute;
    left: 0; right: 0; top: 140px;
    display: flex; align-items: center; justify-content: center; gap: 16px;
  }
  .front-brand .brand-name { font-size: 56px; }
  .front-brand .brand-mark { width: 26px; height: 26px; }
  .front-silhouette {
    position: absolute;
    right: 0; top: 70px;
    width: 170px; height: 230px;
    background: radial-gradient(ellipse at 60% 45%, var(--shadow-grey), rgba(58,58,58,0) 70%);
  }
  .front-band { position: absolute; left: 0; top: 300px; width: 700px; height: 20px; }
  .front-web {
    position: absolute; left: 0; right: 0; top: 340px;
    text-align: center; color: var(--paper);
    font-size: 17px; letter-spacing: 0.5px;
  }

  /* Back */
  .back-brand {
    position: absolute; left: 0; top: 0;
    width: 290px; height: 330px;
    display: flex; align-items: center; justify-content: center; gap: 10px;
  }
  .back-brand .brand-name { font-size: 34px; }
  .back-brand .brand-mark { width: 16px; height: 16px; }
  .back-divider {
    position: absolute; left: 290px; top: 0;
    width: 8px; height: 400px;
    background: linear-gradient(var(--gold-light), var(--gold));
  }
  .back-footer {
    position: absolute; left: 0; bottom: 0;
    width: 290px; height: 70px;
    background: var(--ink);
  }
  .back-footer-line {
    position: absolute; left: 0; top: 18px;
    width: 290px; height: 5px; background: var(--gold);
  }
  .back-silhouette {
    position: absolute; left: 360px; top: 20px;
    width: 330px; height: 170px;
    background: radial-gradient(ellipse at 50% 50%, #dcdcdc, rgba(220,220,220,0) 72%);
  }
  .contact {
    position: absolute; left: 350px; top: 168px;
    color: var(--text-dark);
  }
  .person { display: flex; align-items: center; gap: 12px; margin-bottom: 18px; }
  .person-name { font-size: 22px; font-weight: 700; letter-spacing: 0.5px; }
  .person-title { font-size: 14px; color: #555; margin-top: 2px; }
  .contact-row { display: flex; align-items: center; gap: 12px; margin-bottom: 10px; font-size: 15px; font-weight: 500; }
  .icon {
    width: 26px; height: 26px; border-radius: 50%;
    background: var(--gold);
    display: flex; align-items: center; justify-content: center;
    flex: none;
  }
</style>
</head>
<body>

<section class="card card--front" aria-label="Business card front">
  <div class="front-silhouette" role="img" aria-label="Faint big-cat silhouette decoration"></div>
  <div class="front-brand">
    <span class="brand-mark"></span>
    <span class="brand-name">FALCREST</span>
  </div>
  <svg class="front-band" viewBox="0 0 700 20" aria-hidden="true">
    <defs>
      <linearGradient id="goldBand" x1="0" x2="1">
        <stop offset="0" stop-color="#a87b1e"/>
        <stop offset="0.5" stop-color="#f2d27a"/>
        <stop offset="1" stop-color="#a87b1e"/>
      </linearGradient>
    </defs>
    <polygon points="0,4 300,4 310,16 0,16" fill="url(#goldBand)"/>
    <polygon points="390,4 700,4 700,16 380,16" fill="url(#goldBand)"/>
  </svg>
  <p class="front-web">www.falcrestsecurityservices.example</p>
</section>

<section class="card card--back" aria-label="Business card back">
  <div class="back-brand">
    <span class="brand-mark"></span>
    <span class="brand-name">FALCREST</span>
  </div>
  <div class="back-footer"><div class="back-footer-line"></div></div>
  <div class="back-divider"></div>
  <div class="back-silhouette" role="img" aria-label="Faint big-cat silhouette decoration"></div>

  <div class="contact">
    <div class="person">
      <span class="icon">
        <svg width="14" height="14" viewBox="0 0 14 14" aria-hidden="true"><circle cx="7" cy="4.5" r="3" fill="#fff"/><path d="M1.5 13.5c0-3.2 2.5-5 5.5-5s5.5 1.8 5.5 5z" fill="#fff"/></svg>
      </span>
      <div>
        <div class="person-name">GIL MARSTON</div>
        <div class="person-title">General manager - direct</div>
      </div>
    </div>
    <div class="contact-row">
      <span class="icon">
        <svg width="13" height="13" viewBox="0 0 14 14" aria-hidden="true"><path d="M3 1l2.5 3-1.5 1.5c.8 1.8 2 3 3.5 3.5L9 7.5l3 2.5-1.5 2.5C6 12.5 1.5 8 1.5 3z" fill="#fff"/></svg>
      </span>
      <span>314 862.4490</span>
    </div>
    <div class="contact-row">
      <span class="icon">
        <svg width="14" height="14" viewBox="0 0 14 14" aria-hidden="true"><rect x="1.5" y="3" width="11" height="8" fill="none" stroke="#fff" stroke-width="1.4"/><path d="M1.5 3l5.5 4.5L12.5 3" fill="none" stroke="#fff" stroke-width="1.4"/></svg>
      </span>
      <span>gil@falcrestsecurityservices.example</span>
    </div>
    <div class="contact-row">
      <span class="icon">
        <svg width="14" height="14" viewBox="0 0 14 14" aria-hidden="true"><circle cx="7" cy="7" r="5.5" fill="none" stroke="#fff" stroke-width="1.3"/><path d="M1.5 7h11M7 1.5c-2.5 3-2.5 8 0 11M7 1.5c2.5 3 2.5 8 0 11" fill="none" stroke="#fff" stroke-width="1.1"/></svg>
      </span>
      <span>www.falcrestsecurityservices.example</span>
    </div>
  </div>
</section>

</body>
</html>
```